Need Pexora Ads for Tyre Company

Need some pexora ads graphics for our tyre company Wheel Mates that only operates in the cayman islands.

Need Ratio Ads: 1000x1000, 1910x1000, 300x600

Important things to have the customer know:
-Email : info@wheelmates-demo.ky
-Phone: +1 345 555 0187
-Address: 41 Palmetto Lane, George Town, Cayman Islands
-Website: wheelmates-demo.ky (Please see our website for the tyres we offer)
- Common Car brands that our Tyres are compatible with: Ravello, Korvexa, Pip Talvo, Bexiline, Vardo, Pelmoro, Quendra, Strandmobil
- Our tyres are priced from KYD$55-$60
-We offer free installation on tyres when customers come to our facility to get them changed.
-We sell tyres in bulk and individually.

*You can choose which things to add or omit for the best look, feel free to reword any of the above also to better fit in.
*Please keep in mind that these will have to be viewed in small formats aswell since they are for pexora ads. Please ensure everything is readable when zoomed out.

Target Market(s)

car rental companies & individuals who need to get their tyres replace

Industry/Entity Type

Automotive, Tyre replacement, Car Parts

Colors
EB3D1F
EC4F4E
F09395
F8D3D4
FCEDEE

Requirements
Must have
• Phone, Location, Brands that our tyres are compatible with, Same theme as our logo(Red & Black, White), design adapted to the 3 ratios listed above
Nice to have
• Creative advertising

```html
<!DOCTYPE html>
<html lang="en">
<head>
<meta charset="utf-8">
<title>Wheel Mates – Ad Set</title>
<link href="https://fonts.googleapis.com/css2?family=Audiowide&family=Lato:wght@400;700&display=swap" rel="stylesheet">
<style>
:root{
  --red:#e2261c;
  --ink:#1b1b1b;
  --dark:#232323;
  --grey:#5b5b5b;
  --white:#ffffff;
  --board:#ffffff;
  --display:"Audiowide",sans-serif;
  --body:"Lato",sans-serif;
}
*{box-sizing:border-box;margin:0;padding:0}
html,body{width:1200px;height:439px;overflow:hidden;background:var(--board)}
.board{position:relative;width:1200px;height:439px}
.ad{position:absolute;overflow:hidden;box-shadow:0 1px 4px rgba(0,0,0,.25)}
.abs{position:absolute}
.size-label{position:absolute;font-family:var(--display),sans-serif;color:var(--ink);white-space:nowrap;transform:translateX(-50%)}
.brand-name{font-family:var(--display),sans-serif;white-space:nowrap;display:flex;align-items:center;gap:.3em}
.brand-dot{display:inline-block;border-radius:50%;background:var(--red)}
.tile{position:absolute;background:var(--white);border-radius:2px;display:flex;align-items:center;justify-content:center;font-family:var(--body),sans-serif;font-weight:700;color:var(--ink);text-transform:uppercase;box-shadow:0 1px 2px rgba(0,0,0,.2);overflow:hidden}
.icon{display:inline-block;vertical-align:middle}
.contact{display:flex;align-items:center;white-space:nowrap}
.accent{color:var(--red)}
.link{color:var(--red);text-decoration:underline}

/* square */
.ad-square{left:27px;top:34px;width:343px;height:343px;background:var(--white)}
.sq-call{right:0;top:0;width:116px;height:20px;background:var(--red);clip-path:polygon(5px 0,100% 0,100% 100%,5px 100%,0 50%);color:var(--white);font-family:var(--display),sans-serif;font-size:7px;display:flex;align-items:center;justify-content:center}
.sq-photo{left:175px;top:70px;width:168px;height:202px;background:linear-gradient(160deg,#d9d9d9 0%,#6d6d6d 55%,#4e4e4e 100%);clip-path:polygon(40% 0,100% 0,100% 100%,0 100%,0 95%,30% 60%,20% 20%)}
.sq-text{font-family:var(--display),sans-serif;color:var(--ink)}
.sq-band{left:0;top:271px;width:343px;height:44px;background:var(--red)}
.sq-foot{left:0;top:315px;width:343px;height:28px;background:var(--grey);display:flex;align-items:center;justify-content:space-between;padding:0 7px 0 9px;color:var(--white);font-family:var(--display),sans-serif;font-size:5.2px}

/* wide */
.ad-wide{left:399px;top:34px;width:655px;height:343px;background:var(--white)}
.wd-dark{left:0;top:0;width:655px;height:343px;background:radial-gradient(ellipse at 70% 40%,#333 0%,#1d1d1d 70%);clip-path:polygon(230px 0,100% 0,100% 100%,197px 100%)}
.wd-red{left:0;top:0;width:655px;height:343px;background:var(--red);clip-path:polygon(82px 0,230px 0,197px 100%,49px 100%)}
.wd-tyre{left:24px;top:44px;width:160px;height:260px;border-radius:45% / 50%;background:radial-gradient(ellipse at 62% 50%,#bfc3c7 0%,#8d9196 22%,#2a2a2a 40%,#1a1a1a 100%)}
.wd-foot{left:197px;top:313px;width:458px;height:30px;background:rgba(0,0,0,.25)}
.wd-bullet{font-family:var(--body),sans-serif;color:var(--white);font-size:11px}
.wd-contacts{left:251px;top:318px;width:385px;justify-content:space-between;font-family:var(--display),sans-serif;font-size:5.6px;color:var(--white)}

/* tall */
.ad-tall{left:1072px;top:34px;width:103px;height:206px;background:#f4f4f4}
.tl-dark{left:0;top:27px;width:103px;height:125px;background:linear-gradient(180deg,#262626,#3a3a3a)}
.tl-tread{left:0;top:27px;width:103px;height:19px;background:#101010}
.tl-tyres{left:7px;top:144px;width:89px;height:45px;border-radius:8px;background:linear-gradient(180deg,#4a4a4a,#262626)}
</style>
</head>
<body>
<div class="board">

  <section class="ad ad-square" aria-label="Square ad">
    <div class="abs sq-call">Call Us: +1 345 555 0187</div>
    <div class="abs brand-name" style="left:16px;top:30px;font-size:18px;color:var(--ink)"><span class="brand-dot" style="width:10px;height:10px"></span>Wheel Mates</div>
    <div class="abs sq-photo" role="img" aria-label="Two car tyres on alloy wheels over a tyre-track backdrop"></div>

    <div class="abs sq-text" style="left:17px;top:96px;font-size:11px">Our tyres are priced from</div>
    <div class="abs sq-text accent" style="left:17px;top:117px;font-size:14px">KYD$55-$60</div>

    <div class="abs sq-text" style="left:17px;top:143px;font-size:7px;line-height:14px;width:150px">
      <svg class="icon" width="8" height="8" viewBox="0 0 10 10"><circle cx="5" cy="5" r="3.8" fill="none" stroke="var(--ink)" stroke-width="1.6"/></svg>
      We offer free installation on tyres when customers come to our facility to get them changed.
    </div>
    <div class="abs sq-text" style="left:17px;top:197px;font-size:7px">
      <svg class="icon" width="8" height="8" viewBox="0 0 10 10"><circle cx="5" cy="5" r="3.8" fill="none" stroke="var(--ink)" stroke-width="1.6"/></svg>
      We sell tyres in bulk and individually
    </div>
    <div class="abs contact sq-text" style="left:17px;top:243px;font-size:8px;gap:5px">
      <svg width="10" height="10" viewBox="0 0 10 10"><circle cx="5" cy="5" r="4.2" fill="none" stroke="var(--red)" stroke-width=".8"/><ellipse cx="5" cy="5" rx="1.8" ry="4.2" fill="none" stroke="var(--red)" stroke-width=".8"/><path d="M1 5h8" stroke="var(--red)" stroke-width=".8"/></svg>
      <span class="link">wheelmates-demo.ky</span>
    </div>

    <div class="abs sq-band">
      <div class="tile" style="left:18px;top:9px;width:33px;height:25px;font-size:4.5px">Ravello</div>
      <div class="tile" style="left:58px;top:9px;width:33px;height:25px;font-size:4.5px">Korvexa</div>
      <div class="tile" style="left:98px;top:9px;width:33px;height:25px;font-size:4.5px">Talvo</div>
      <div class="tile" style="left:138px;top:9px;width:33px;height:25px;font-size:4px">Bexiline</div>
      <div class="tile" style="left:178px;top:9px;width:33px;height:25px;font-size:4.5px">Vardo</div>
      <div class="tile" style="left:218px;top:9px;width:33px;height:25px;font-size:4.5px">Pelmoro</div>
      <div class="tile" style="left:258px;top:9px;width:33px;height:25px;font-size:4.5px">Quendra</div>
      <div class="tile" style="left:298px;top:9px;width:33px;height:25px;font-size:3.6px">Strandmobil</div>
    </div>

    <div class="abs sq-foot">
      <span class="contact" style="gap:3px"><svg width="7" height="5" viewBox="0 0 8 6"><rect width="8" height="6" fill="var(--red)"/><path d="M0 0l4 3.2L8 0" fill="none" stroke="var(--grey)" stroke-width=".8"/></svg>info@wheelmates-demo.ky</span>
      <span class="contact" style="gap:3px"><svg width="6" height="6" viewBox="0 0 10 10"><path d="M2 1l2 2-1 1.5c.8 1.5 1.8 2.5 3.5 3.5L8 6l2 2-1.5 1.8C5 9.5 .5 5 .2 1.5z" fill="var(--red)"/></svg>+1 345 555 0187</span>
      <span class="contact" style="gap:3px"><svg width="5" height="7" viewBox="0 0 6 8"><path d="M3 0a3 3 0 0 1 3 3c0 2-3 5-3 5S0 5 0 3a3 3 0 0 1 3-3z" fill="var(--red)"/><circle cx="3" cy="3" r="1" fill="var(--grey)"/></svg>41 Palmetto Lane, George Town, Cayman Islands</span>
    </div>
  </section>
  <div class="size-label" style="left:199px;top:403px;font-size:13px">1000 x1000</div>

  <section class="ad ad-wide" aria-label="Wide ad">
    <div class="abs wd-dark"></div>
    <div class="abs wd-red"></div>
    <div class="abs wd-tyre" role="img" aria-label="Single car tyre on a silver alloy wheel"></div>
    <div class="abs wd-foot"></div>

    <div class="abs brand-name" style="left:251px;top:66px;font-size:30px;color:var(--white)"><span class="brand-dot" style="width:16px;height:16px"></span>Wheel Mates</div>

    <div class="abs" style="left:251px;top:117px;font-family:var(--display),sans-serif;font-size:17px;color:var(--white);white-space:nowrap">Our tyres are priced from <span class="accent">KYD$55-$60</span></div>

    <div class="abs wd-bullet" style="left:251px;top:152px;width:370px;line-height:24px">
      <svg class="icon" width="13" height="13" viewBox="0 0 10 10" style="margin-right:5px"><circle cx="5" cy="5" r="3.8" fill="none" stroke="var(--white)" stroke-width="1.4"/></svg>We offer free installation on tyres when customers come to our facility to get them changed.
    </div>
    <div class="abs wd-bullet" style="left:251px;top:207px">
      <svg class="icon" width="13" height="13" viewBox="0 0 10 10" style="margin-right:5px"><circle cx="5" cy="5" r="3.8" fill="none" stroke="var(--white)" stroke-width="1.4"/></svg>We sell tyres in bulk and individually.
    </div>

    <div class="tile" style="left:252px;top:242px;width:38px;height:29px;font-size:5px">Ravello</div>
    <div class="tile" style="left:298px;top:242px;width:38px;height:29px;font-size:5px">Korvexa</div>
    <div class="tile" style="left:344px;top:242px;width:38px;height:29px;font-size:5px">Talvo</div>
    <div class="tile" style="left:390px;top:242px;width:38px;height:29px;font-size:4.6px">Bexiline</div>
    <div class="tile" style="left:436px;top:242px;width:38px;height:29px;font-size:5px">Vardo</div>
    <div class="tile" style="left:482px;top:242px;width:38px;height:29px;font-size:5px">Pelmoro</div>
    <div class="tile" style="left:528px;top:242px;width:38px;height:29px;font-size:5px">Quendra</div>
    <div class="tile" style="left:574px;top:242px;width:38px;height:29px;font-size:4px">Strandmobil</div>

    <div class="abs contact" style="left:251px;top:289px;gap:5px;font-family:var(--display),sans-serif;font-size:8px">
      <svg width="10" height="10" viewBox="0 0 10 10"><circle cx="5" cy="5" r="4.2" fill="none" stroke="var(--red)" stroke-width=".8"/><ellipse cx="5" cy="5" rx="1.8" ry="4.2" fill="none" stroke="var(--red)" stroke-width=".8"/><path d="M1 5h8" stroke="var(--red)" stroke-width=".8"/></svg>
      <span style="color:var(--white);text-decoration:underline">wheelmates-demo.ky</span>
    </div>

    <div class="abs contact wd-contacts">
      <span class="contact" style="gap:4px"><svg width="8" height="6" viewBox="0 0 8 6"><rect width="8" height="6" fill="var(--red)"/><path d="M0 0l4 3.2L8 0" fill="none" stroke="var(--dark)" stroke-width=".8"/></svg>info@wheelmates-demo.ky</span>
      <span class="contact" style="gap:4px"><svg width="7" height="7" viewBox="0 0 10 10"><path d="M2 1l2 2-1 1.5c.8 1.5 1.8 2.5 3.5 3.5L8 6l2 2-1.5 1.8C5 9.5 .5 5 .2 1.5z" fill="var(--red)"/></svg>+1 345 555 0187</span>
      <span class="contact" style="gap:4px"><svg width="6" height="8" viewBox="0 0 6 8"><path d="M3 0a3 3 0 0 1 3 3c0 2-3 5-3 5S0 5 0 3a3 3 0 0 1 3-3z" fill="var(--red)"/><circle cx="3" cy="3" r="1" fill="var(--dark)"/></svg>41 Palmetto Lane, George Town, Cayman Islands</span>
    </div>
  </section>
  <div class="size-label" style="left:727px;top:407px;font-size:13px">1910x1000</div>

  <section class="ad ad-tall" aria-label="Tall ad">
    <div class="abs brand-name" style="left:50%;top:8px;transform:translateX(-50%);font-size:8px;color:var(--ink)"><span class="brand-dot" style="width:5px;height:5px"></span>Wheel Mates</div>
    <div class="abs tl-dark"></div>
    <div class="abs tl-tread" role="img" aria-label="Tyre tread print band"></div>
    <div class="abs" style="left:0;top:53px;width:103px;text-align:center;font-family:var(--display),sans-serif;font-size:5.5px;color:var(--white)">Our tyres are priced from</div>
    <div class="abs accent" style="left:0;top:63px;width:103px;text-align:center;font-family:var(--display),sans-serif;font-size:5px">KYD$55-$60</div>
    <div class="abs" style="left:11px;top:75px;width:86px;font-family:var(--display),sans-serif;font-size:3.6px;line-height:8px;color:var(--white)">
      <svg class="icon" width="5" height="5" viewBox="0 0 10 10"><circle cx="5" cy="5" r="3.8" fill="none" stroke="var(--white)" stroke-width="1.6"/></svg>
      We offer free installation on tyres when customers come to our facility to get them changed.
    </div>
    <div class="abs" style="left:11px;top:103px;font-family:var(--display),sans-serif;font-size:3.6px;color:var(--white);white-space:nowrap">
      <svg class="icon" width="5" height="5" viewBox="0 0 10 10"><circle cx="5" cy="5" r="3.8" fill="none" stroke="var(--white)" stroke-width="1.6"/></svg>
      We sell tyres in bulk and individually
    </div>
    <div class="tile" style="left:18px;top:117px;width:11px;height:8px;font-size:1.6px">Ravello</div>
    <div class="tile" style="left:32px;top:117px;width:11px;height:8px;font-size:1.6px">Korvexa</div>
    <div class="tile" style="left:46px;top:117px;width:11px;height:8px;font-size:1.8px">Talvo</div>
    <div class="tile" style="left:60px;top:117px;width:11px;height:8px;font-size:1.5px">Bexiline</div>
    <div class="tile" style="left:74px;top:117px;width:11px;height:8px;font-size:1.8px">Vardo</div>
    <div class="tile" style="left:32px;top:130px;width:11px;height:8px;font-size:1.6px">Quendra</div>
    <div class="tile" style="left:46px;top:130px;width:11px;height:8px;font-size:1.2px">Strandmobil</div>
    <div class="tile" style="left:60px;top:130px;width:11px;height:8px;font-size:1.6px">Pelmoro</div>
    <div class="abs tl-tyres" role="img" aria-label="Row of four car tyres on alloy wheels"></div>
    <div class="abs link" style="left:0;top:192px;width:103px;text-align:center;font-family:var(--display),sans-serif;font-size:2.8px">wheelmates-demo.ky</div>
    <div class="abs" style="left:0;top:199px;width:103px;text-align:center;font-family:var(--display),sans-serif;font-size:2px;color:var(--ink);white-space:nowrap">info@wheelmates-demo.ky &nbsp; +1 345 555 0187 &nbsp; 41 Palmetto Lane, George Town</div>
  </section>
  <div class="size-label" style="left:1124px;top:259px;font-size:9px">300x600</div>

</div>
</body>
</html>
```